KRV Inc Web Design

WHAT ARE WE DOING?
We are developing a new website look and feel for a new company called KRV Inc. This new look and feel should include colors, design elements, choice of photography and other imagery, fonts, and other user experience elements.

WHAT DO THEY DO?
KRV, Inc, makes tools for researchers who are studying protein-protein interactions. These molecules are the basic tools of biology, and serve as key targets for drug developers and disease researchers. The world of proteins is enormously complex, and companies like KRV provide researchers with critical tools that help them elucidate this world.

WHO ARE WE TALKING TO?
The target audience for this website are professional scientists working in university research or biopharma drug development. They are highly sophisticated consumers looking for key tools that will advance their research.

WHAT DO WE WANT THEM TO DO?
The site is an information resource for the customer exploring the tools that KRV sells and the scientific issues surrounding protein-protein interactions. They should be able to navigate easily to their content of choice, while the whole site should convey a professionalism that enhanced KRV’s credibility.

WHAT DOES THE KRV BRAND STAND FOR?
KRV stands for illumination. Proteins are challenging to study, and KRV exists to help shed light on their workings.

WHAT ARE THE KEY VALUES OF THE KRV BRAND?
Integrity. Innovation. Insight.

WHAT ARE THE EXECUTIONAL MANDITORIES?
The look and feel is completely up for grabs. Nothing is off the table.

WHAT ARE THE DELIVERABLES?
We need new designs for the following templates:
http://cms.thevormelgroup.com/
http://cms.thevormelgroup.com/products-and-services/instruments-3/bench-top-instruments/
http://cms.thevormelgroup.com/category/lab-study/

```html
<!DOCTYPE html>
<html lang="en">
<head>
<meta charset="utf-8">
<title>KRV Inc</title>
<link href="https://fonts.googleapis.com/css2?family=Source+Sans+3:wght@400;600&display=swap" rel="stylesheet">
<style>
:root{
  --blue:#4a9fdc;
  --blue-soft:#a9d7e4;
  --ink:#333;
  --ink-soft:#555;
  --topbar:#f6f6f6;
  --header:#ececec;
  --band:#f3f3f3;
  --page:#f1f1f1;
  --panel:#fff;
  --teal:#b4ded6;
  --caption:#5c6b67;
  --btn:#f0f0f0;
  --btn-border:#c9c9c9;
}
*{margin:0;padding:0;box-sizing:border-box}
html,body{width:1106px;height:1200px;overflow:hidden}
body{position:relative;background:var(--page);font-family:"Source Sans 3",sans-serif;color:var(--ink)}
.abs{position:absolute}
.topbar{left:0;top:0;width:1106px;height:22px;background:var(--topbar)}
.phone{left:780px;top:3px;color:var(--blue);font-size:13px;display:flex;align-items:center;gap:4px}
.header-band{left:0;top:22px;width:1106px;height:112px;background:var(--header)}
.light-band{left:0;top:134px;width:1106px;height:62px;background:var(--band)}
.hero-band{left:0;top:196px;width:1106px;height:212px;background:var(--header);border-bottom:1px solid #d4d4d4}
.logo{left:232px;top:52px;display:flex;align-items:center;gap:8px;color:var(--blue);font-size:44px;font-weight:600;line-height:1}
.logo .dot{width:22px;height:22px;background:var(--blue-soft);border-radius:50%}
.social{width:24px;height:24px;border-radius:50%;background:var(--blue)}
.search{left:690px;top:48px;width:186px;height:25px;background:#fff;font-size:8.5px;color:#aaa;padding:7px 6px}
.search svg{position:absolute;right:8px;top:6px}
.nav{left:450px;top:104px;font-size:11px;color:var(--ink)}
.nav span{position:absolute;white-space:nowrap}
.nav .active{color:var(--blue);border-bottom:2px solid var(--blue);padding-bottom:2px}
.dropdown{left:450px;top:129px;width:101px;height:66px;background:#fff;border:1px solid #ddd;font-size:8.5px;padding:6px 8px;z-index:3}
.dropdown div{height:18px;line-height:16px}
.dropdown .on{color:var(--blue)}
.dropdown .on span{border-bottom:1px solid var(--blue)}
.hero{left:230px;top:167px;width:645px;height:203px;background:var(--teal)}
.hero-photo{left:500px;top:167px;width:375px;height:203px;background:linear-gradient(90deg,#b4ded6,#dde8ea 30%,#eef1f3 60%,#cfdfe2)}
.caption{left:230px;top:272px;width:236px;height:89px;background:var(--caption);color:#fff;font-size:10.5px;line-height:13.5px;padding:14px 14px}
.btn{position:absolute;background:var(--btn);border:1px solid var(--btn-border);font-size:8.5px;color:var(--ink);text-align:center;line-height:17px}
.panel{left:230px;top:386px;width:645px;height:766px;background:var(--panel)}
h2{position:absolute;color:var(--blue);font-weight:400;font-size:12.5px;white-space:nowrap}
p.body{position:absolute;font-size:8.3px;line-height:11.1px;color:var(--ink)}
.vdots{left:676px;top:412px;height:72px;border-left:1px dotted var(--blue)}
.divider{left:238px;width:631px;border-top:2px dotted var(--blue)}
.input{left:690px;top:414px;width:171px;height:24px;background:#f0f0f0;border:1px solid #d6d6d6}
.card-img{top:526px;width:204px;height:125px;border:1px solid #ccc}
.icon-circle{width:70px;height:70px;border-radius:50%;background:var(--blue)}
.footer{left:0;top:1138px;width:1106px;height:62px;background:var(--page);border-top:1px solid #ddd}
.footer-links{left:232px;top:1166px;font-size:8.5px;color:var(--ink);white-space:nowrap;word-spacing:1px}
.footer-links i{font-style:normal;margin:0 8px}
.footer-social{width:26px;height:26px;border-radius:50%;background:#111}
</style>
</head>
<body>
<div class="abs topbar"></div>
<div class="abs phone">
  <svg width="12" height="14" viewBox="0 0 12 14"><path d="M2 1c1-.6 2 .2 2.4 1.2l.8 2c.3.8-.2 1.4-.8 1.8.6 1.6 1.6 2.9 3 3.8.5-.6 1.2-.9 1.9-.5l1.7 1c.9.5 1.1 1.5.4 2.2-.8.8-2 1.1-3.1.6C4.6 11.8 1.6 8 .8 4.3.6 3 1 1.7 2 1z" fill="#4a9fdc"/></svg>
  + 000 000 000
</div>
<div class="abs header-band"></div>
<div class="abs light-band"></div>
<div class="abs hero-band"></div>

<div class="abs logo"><span class="dot"></span>KRV INC</div>
<div class="abs social" style="left:627px;top:48px"></div>
<div class="abs social" style="left:658px;top:48px"></div>
<div class="abs search">Search the Site
  <svg width="12" height="12" viewBox="0 0 12 12"><circle cx="5" cy="5" r="4" fill="none" stroke="#aaa" stroke-width="1.2"/><line x1="8" y1="8" x2="11" y2="11" stroke="#aaa" stroke-width="1.2"/></svg>
</div>

<nav class="abs nav">
  <span class="active" style="left:0">Company</span>
  <span style="left:64px">Products &amp; Services</span>
  <span style="left:172px">Learning Center</span>
  <span style="left:264px">Events</span>
  <span style="left:316px">KRV News</span>
  <span style="left:377px">Contact Us</span>
</nav>
<div class="abs dropdown">
  <div>Locations</div>
  <div class="on"><span>Quality Leadership</span></div>
  <div>Community</div>
</div>

<div class="abs hero"></div>
<div class="abs hero-photo" role="img" aria-label="Photo of two scientists in a laboratory working with a microscope"></div>
<div class="abs caption">The Majority of GPCR-based drug discovery programs have failed to yield highly Selective compounds.</div>
<div class="btn" style="left:367px;top:325px;width:75px;height:18px">Learn more</div>

<div class="abs panel"></div>

<h2 style="left:244px;top:395px">WELCOME TO KRV INC</h2>
<p class="body" style="left:244px;top:419px;width:412px">Lorem Ipsum is simply dummy text of the printing and typesetting industry. Lorem Ipsum has been the industry's standard dummy text ever since the 1500s, when an unknown printer took a galley of type and scrambled it to make a type specimen book. It has survived not only five centuries, but also the leap into electronic typesetting, remaining essentially unchanged. It was popularised in the 1960s with the release of Veltrane sheets containing Lorem Ipsum passages, and more recently with desktop publishing software like Orlin PageSet including versions of Lorem Ipsum.</p>
<div class="abs vdots"></div>

<h2 style="left:690px;top:395px">NEWSLETTER</h2>
<div class="abs input"></div>
<p class="body" style="left:690px;top:443px;width:180px;font-size:7.5px;line-height:14px">- Corporate Headquarter 04100-2020.<br>- KRV South (800) 555-0142.</p>
<div class="btn" style="left:817px;top:471px;width:44px;height:19px">SEND</div>

<div class="abs divider" style="top:502px"></div>

<div class="abs card-img" style="left:238px;background:linear-gradient(180deg,#fafafa,#eee)" role="img" aria-label="Hand placing a letter into the word innovation"></div>
<div class="abs card-img" style="left:451px;background:linear-gradient(180deg,#c7d9e6,#e9eef2 60%,#bcd0dc)" role="img" aria-label="Rack of laboratory test tubes"></div>
<div class="abs card-img" style="left:665px;background:linear-gradient(90deg,#e8ecef,#c9d3d9 50%,#eef0f1)" role="img" aria-label="Researcher writing notes beside a microscope"></div>

<h2 style="left:244px;top:659px">INNOVATION</h2>
<p class="body" style="left:244px;top:677px;width:190px">Lorem ipsum dolor sit amet, consectetur adipisc-ing elit. Proin placerat nulla massa, a condimen-tum leo tincidunt vel.<br><br>Consectetur adipiscing elit. Proin placerat nulla massa, a condimentum leo.</p>
<div class="btn" style="left:302px;top:753px;width:76px;height:19px">Learn more</div>

<h2 style="left:456px;top:659px">AUTOMATION</h2>
<p class="body" style="left:456px;top:677px;width:194px">Lorem ipsum dolor sit amet, consectetur adipisc-ing elit. Aenean facilisis interdum. Vivamus et sapien varius.<br><br>Dolor sit amet, consectetur adipiscing elit. Aenean facilisis interdum.</p>
<div class="btn" style="left:515px;top:753px;width:76px;height:19px">Order Today</div>

<h2 style="left:672px;top:659px">RESEARCH</h2>
<p class="body" style="left:672px;top:677px;width:194px">Lorem ipsum dolor sit amet, consectetur adipisc-ing elit. Class aptent taciti sociosqu ad litora torquent per conubia.<br><br>Amet, consectetur adipiscing elit. Class aptent taciti sociosqu ad litora torquent per.</p>
<div class="btn" style="left:729px;top:753px;width:76px;height:19px">The Challenge</div>

<div class="abs divider" style="top:788px"></div>

<h2 style="left:312px;top:824px">MICROSCOPE</h2>
<p class="body" style="left:312px;top:845px;width:370px">Lorem Ipsum is simply dummy text of the printing and typesetting industry. Lorem Ipsum has been the industry's standard dummy text ever since the 1500s, when an unknown printer took a galley of type and scrambled it to make a type specimen book.</p>
<div class="abs icon-circle" style="left:724px;top:816px" role="img" aria-label="Microscope icon"></div>

<div class="abs divider" style="top:908px"></div>

<div class="abs icon-circle" style="left:314px;top:929px" role="img" aria-label="Flask icon"></div>
<h2 style="left:432px;top:937px">DRUG</h2>
<p class="body" style="left:432px;top:957px;width:370px">Lorem Ipsum is simply dummy text of the printing and typesetting industry. Lorem Ipsum has been the industry's standard dummy text ever since the 1500s, when an unknown printer took a galley of type and scrambled it to make a type specimen book.</p>

<div class="abs divider" style="top:1025px"></div>

<h2 style="left:312px;top:1049px">SYRINGE</h2>
<p class="body" style="left:312px;top:1069px;width:370px">Lorem Ipsum is simply dummy text of the printing and typesetting industry. Lorem Ipsum has been the industry's standard dummy text ever since the 1500s, when an unknown printer took a galley of type and scrambled it to make a type specimen book.</p>
<div class="abs icon-circle" style="left:724px;top:1040px" role="img" aria-label="Syringe icon"></div>

<div class="abs divider" style="top:1137px"></div>

<footer class="abs footer"></footer>
<div class="abs footer-links">Home<i>|</i>Company<i>|</i>Products &amp; Services<i>|</i>Contact Us<i>|</i>Site Map<i>|</i>Privacy Policy<i>|</i>Terms © 2013 Demo Site</div>
<div class="abs footer-social" style="left:813px;top:1160px"></div>
<div class="abs footer-social" style="left:843px;top:1160px"></div>
</body>
</html>
```